Chiropractic Flyers to be made more up to date

I have used this series of flyers for my own practice. I would like the graphics to be brought up to date and the name of the doctor and the practice, the address, phone number and date to be removed and a blank box inserted in one place on the flyer that other chiropractors could use to personalize the flyers for their practice. On some of the flyers, this information is in several places. I'd like to have it all in one space so that it would be easy for the doctor to add it in their practice. They all need to be bright and colorful with catchy graphics.

```html
<!DOCTYPE html>
<html lang="en">
<head>
<meta charset="UTF-8">
<title>Backpack Safety Demonstration</title>
<link rel="stylesheet" href="https://fonts.googleapis.com/css2?family=Oswald:wght@500;700&family=Lato:wght@400;700&display=swap">
<style>
  :root {
    --red: #c9464b;
    --red-dark: #a8343a;
    --ink: #2c2c2c;
    --panel: #333232;
    --yellow: #f3e266;
    --badge-yellow: #f5e23a;
    --white: #ffffff;
    --text-grey: #4a4a4a;
    --ray: #ececec;
    --bag-blue: #4a3fa0;
  }
  * { margin: 0; padding: 0; box-sizing: border-box; }
  html, body { width: 930px; height: 1200px; overflow: hidden; background: var(--white); }
  .flyer {
    position: relative;
    width: 930px; height: 1200px;
    background: var(--white);
    font-family: 'Lato', sans-serif;
    overflow: hidden;
  }
  .hero-glow {
    position: absolute; top: 185px; left: 0; width: 930px; height: 440px; z-index: 0;
    background: radial-gradient(ellipse at 50% 50%, #ffffff 0%, #f6f6f6 35%, var(--ray) 60%, #ffffff 85%);
  }
  .top-tab { position: absolute; top: 0; left: 300px; width: 340px; height: 10px; background: var(--red); z-index: 2; }
  .foot-bar { position: absolute; bottom: 0; height: 12px; background: var(--red); z-index: 2; }
  .foot-bar.left { left: 0; width: 275px; }
  .foot-bar.right { right: 0; width: 277px; }

  .title {
    position: absolute; top: 42px; left: 0; width: 100%; z-index: 2;
    text-align: center;
    font-family: 'Oswald', sans-serif; font-weight: 700;
    font-size: 87px; line-height: 1.1; color: var(--red);
    letter-spacing: 1px;
  }
  .subtitle {
    position: absolute; top: 130px; left: 0; width: 100%; z-index: 2;
    text-align: center;
    font-family: 'Oswald', sans-serif; font-weight: 500;
    font-size: 38px; line-height: 1.2; color: var(--ink);
    letter-spacing: 0.86em; padding-left: 0.86em;
  }
  .hero-bag {
    position: absolute; left: 290px; top: 208px; width: 338px; height: 398px; z-index: 1;
    border-radius: 120px 120px 40px 40px;
    background: linear-gradient(160deg, #d8454c 0%, #c2323a 60%, #9e262c 100%);
    box-shadow: 0 14px 18px -10px rgba(0,0,0,0.35);
  }
  .badge { position: absolute; left: 540px; top: 265px; width: 230px; height: 230px; z-index: 2; }
  .badge-text {
    position: absolute; left: 540px; top: 265px; width: 230px; height: 230px; z-index: 3;
    display: flex; flex-direction: column; align-items: center; justify-content: center;
    text-align: center;
  }
  .badge-main { font-family: 'Oswald', sans-serif; font-weight: 700; font-size: 33px; line-height: 1; color: var(--badge-yellow); }
  .badge-sub { font-family: 'Lato', sans-serif; font-size: 20px; line-height: 1; color: var(--white); margin-top: 8px; }

  .info-panel { position: absolute; left: 28px; top: 612px; width: 872px; height: 254px; z-index: 2; }
  .info-panel svg { position: absolute; inset: 0; }
  .benefits {
    position: absolute; left: 47px; top: 64px; right: 20px;
    list-style: none;
  }
  .benefits li {
    position: relative; padding-left: 26px;
    font-weight: 700; font-size: 24px; line-height: 28px; color: var(--white);
    margin-bottom: 20px;
  }
  .benefits li::before {
    content: ""; position: absolute; left: 0; top: 8px;
    width: 13px; height: 13px; border-radius: 50%; background: var(--yellow);
  }

  .invite-heading {
    position: absolute; left: 28px; top: 894px; z-index: 2;
    font-family: 'Oswald', sans-serif; font-weight: 700;
    font-size: 52px; line-height: 1.1; color: var(--ink);
  }
  .invite-heading .accent { color: var(--red); }
  .invite-copy { position: absolute; left: 28px; top: 962px; width: 630px; z-index: 2; }
  .invite-copy p { font-size: 17px; line-height: 22px; color: var(--text-grey); margin-bottom: 14px; }

  .side-bag {
    position: absolute; left: 660px; top: 900px; width: 220px; height: 275px; z-index: 1;
    border-radius: 60px 90px 30px 30px;
    background: linear-gradient(150deg, #5a4fb8 0%, var(--bag-blue) 55%, #2f2876 100%);
    box-shadow: 16px 0 0 -4px var(--red-dark);
  }
</style>
</head>
<body>
<main class="flyer">
  <div class="hero-glow"></div>
  <div class="top-tab"></div>

  <h1 class="title">BACKPACK SAFETY</h1>
  <p class="subtitle">DEMONSTRATION</p>

  <div class="hero-bag" role="img" aria-label="Illustration of a red school backpack with a yellow front pocket and pencils"></div>

  <svg class="badge" viewBox="0 0 230 230" aria-hidden="true">
    <polygon fill="#2c2c2c" points="
      115,0 124,20 139,3 143,25 161,11 160,33 181,23 175,45 197,40 186,60 209,60 194,77 215,84 196,95 214,108 195,115 214,122 196,135 215,146 194,153 209,170 186,170 197,190 175,185 181,207 160,197 161,219 143,205 139,227 124,210 115,230 106,210 91,227 87,205 69,219 70,197 49,207 55,185 33,190 44,170 21,170 36,153 15,146 34,135 16,122 35,115 16,108 34,95 15,84 36,77 21,60 44,60 33,40 55,45 49,23 70,33 69,11 87,25 91,3 106,20"/>
    <circle cx="115" cy="115" r="84" fill="#2c2c2c" stroke="#ffffff" stroke-width="3"/>
  </svg>
  <div class="badge-text">
    <span class="badge-main">STAND UP</span>
    <span class="badge-sub">FOR SUCESS</span>
  </div>

  <section class="info-panel">
    <svg viewBox="0 0 872 254" aria-hidden="true">
      <path fill="#333232" d="M24,0 H222 V10 Q222,36 248,36 H622 Q648,36 648,10 V0 H848 Q872,0 872,24 V230 Q872,254 848,254 H24 Q0,254 0,230 V24 Q0,0 24,0 Z"/>
    </svg>
    <ul class="benefits">
      <li>Learn how your posture can effect your attitude and self-esteem.</li>
      <li>Learn the posture of a “Winner” &amp; how to avoid the posture<br>of a “Loser”.</li>
      <li>Learn proper backpack safety to stand up for success.</li>
    </ul>
  </section>

  <h2 class="invite-heading"><span class="accent">PARENTS &amp;</span> FACULTY INVITED</h2>
  <div class="invite-copy">
    <p>Lorem Ipsum is simply dummy text of the printing and typesetting industry. Lorem Ipsum has been the industry's standard dummy text ever since the 1500s, when an unknown printer took a galley of type and scrambled it to make a type specimen book.</p>
    <p>Lorem Ipsum is simply dummy text of the printing and typesetting industry. Lorem Ipsum has been the industry's standard dummy text ever since the 1500s, when an unknown printer took a galley of type and scrambled it to make a type specimen book.</p>
  </div>

  <div class="side-bag" role="img" aria-label="Illustration of a blue backpack with a red strap"></div>

  <div class="foot-bar left"></div>
  <div class="foot-bar right"></div>
</main>
</body>
</html>
```